Travel video blogger needs website design

I need a website designed for my new travel video blog "Roaming Sparrow". I have only just started but need a website that is fairly simple and not too busy. I have a logo which I want on it (I have attached it to this project). I also want a link to all my other social medias on the main page (vidtrekhub, Snapwell and Palnook) and my videos as well. Here is a link to my vidtrekhub page for you to look at: https://www.vidtrekhub.net/channel/QRm4tZ8pWnE2HX57YKccd31v
As I have only just started and I am still trying to find my specific niche, again I need it to be sleek and simple that I can go in and change slightly here and there. I would like these pages on the website: About Me, Videos, Social Media, Blog, Gallery, contact me. for an example I like the look of www.theroamingkinfolk.net website.

I already have the domain and I am with Harborweb with pagecraftr.org. I just want to spend my time getting better and learning about videos then trying to create a website (I am a bit of a perfectionist when I try to do something).

Target Market(s)

Young Adults (majority females) between the ages of 18 and 30 with an interest in travelling.

Industry/Entity Type

Travel Industry

Number of Pages Required

1 page

Colors

Designer to choose colors to be used in the design.

Requirements
Must have
• A like to my Snapwell, Palnook and vidtrekhub channels on the home page
• Must be a nice, simple design
• Must have my logo on the front and name "Roaming Sparrow"
Nice to have
• A nice light, bright coloured theme
Should not have
• A dark coloured theme

```html
<!DOCTYPE html>
<html lang="en">
<head>
<meta charset="utf-8">
<title>Roaming Sparrow</title>
<link href="https://fonts.googleapis.com/css2?family=Open+Sans:wght@400;600;700&family=Montserrat:wght@800&display=swap" rel="stylesheet">
<style>
:root{
  --ink:#111;
  --muted:#8a8a8a;
  --nav:#333;
  --rule:#cfcfcf;
  --bg:#fff;
  --label:#fff;
}
*{margin:0;padding:0;box-sizing:border-box}
html,body{width:890px;height:1200px;overflow:hidden;background:var(--bg)}
body{position:relative;font-family:"Open Sans",Arial,sans-serif;color:var(--ink)}
a{text-decoration:none;color:inherit}
.abs{position:absolute}
.brand{display:flex;flex-direction:column;align-items:center;gap:6px}
.brand-dot{width:34px;height:34px;border-radius:50%;border:1.5px solid var(--ink)}
.brand-name{font-weight:600;font-size:10.5px;letter-spacing:.6px;color:var(--ink)}
.site-brand{left:187px;top:10px;width:88px}
.socials{display:flex;gap:8px;align-items:center}
.social{display:flex;align-items:center;gap:3px;font-size:8px;color:var(--ink)}
.social i{width:14px;height:14px;border-radius:50%;background:var(--ink);display:block}
.top-socials{right:188px;top:31px}
.main-nav{right:186px;top:61px;display:flex;gap:17px;font-size:8px}
.main-nav a{color:var(--muted)}
.main-nav a.active{color:var(--nav)}
.hero{left:187px;top:87px;width:517px;height:174px;
  background:linear-gradient(100deg,#e7dbd8 0%,#b9a7a9 35%,#8d7f83 55%,#d9b79b 80%,#f2c38e 100%)}
.tile{width:165px;height:109px;display:flex;align-items:center;justify-content:center}
.tile span{font-family:"Montserrat",Arial,sans-serif;font-weight:800;font-size:15px;letter-spacing:1px;color:var(--label)}
.t-santorini{background:linear-gradient(160deg,#4f83b8,#7fa9cf 45%,#d6dbe4 70%,#9a6b7c)}
.t-paris{background:linear-gradient(170deg,#2b5a8c,#5d8fbf 50%,#6a6552 90%)}
.t-india{background:linear-gradient(180deg,#8f958d,#a49a89 60%,#b7a48e)}
.t-turkey{background:linear-gradient(170deg,#c8d3df,#d8d2c6 50%,#a9a59e)}
.t-england{background:linear-gradient(180deg,#6e7a86,#4c4f53 60%,#26292c)}
.t-germany{background:linear-gradient(180deg,#3e72b0,#8aa7b8 40%,#4d7d3a 75%,#2f5a24)}
.section-title{left:0;width:890px;top:755px;text-align:center;font-size:12px;font-weight:400;letter-spacing:1.2px;color:var(--ink)}
.video{display:flex;align-items:center;justify-content:center}
.v-main{left:187px;top:789px;width:257px;height:204px;background:linear-gradient(180deg,#6fa6d8,#bcd6ea 50%,#5f9bc1 62%,#3f7ea6)}
.v-dusk{left:445px;top:789px;width:128px;height:101px;background:linear-gradient(180deg,#b99a5e,#d9b270 50%,#7f8d93 70%,#4a6b82)}
.v-lake{left:574px;top:789px;width:128px;height:101px;background:linear-gradient(180deg,#b87a3a,#3aa3c4 50%,#2b7f9a 70%,#9a6a2f)}
.v-town{left:445px;top:892px;width:128px;height:101px;background:linear-gradient(180deg,#2f4c8c,#4a4a6a 50%,#c59f66 70%,#3a3a45)}
.v-all{left:574px;top:892px;width:128px;height:101px;background:linear-gradient(180deg,#4f514d,#3a3c38);flex-direction:column;gap:5px;text-decoration:none}
.v-all span{color:#fff;font-size:8px;font-weight:700;letter-spacing:.8px;text-decoration:none}
.v-all b{width:42px;height:1px;background:#fff;opacity:.6}
.footer-rule{left:194px;top:1024px;width:503px;height:1px;background:var(--rule)}
.footer-brand{left:0;width:890px;top:1048px}
.footer-nav{left:0;width:890px;top:1117px;display:flex;justify-content:center;gap:16px;font-size:8px}
.footer-nav a{color:var(--nav)}
.footer-socials{left:0;width:890px;top:1144px;justify-content:center}
.copyright{left:0;width:890px;top:1174px;text-align:center;font-size:6px;color:var(--muted)}
</style>
</head>
<body>
<header>
  <div class="abs brand site-brand"><span class="brand-dot"></span><span class="brand-name">ROAMINGSPARROW</span></div>
  <div class="abs socials top-socials">
    <a class="social" href="#"><i></i>Snapwell</a>
    <a class="social" href="#"><i></i>Palnook</a>
    <a class="social" href="#"><i></i>vidtrekhub</a>
  </div>
  <nav class="abs main-nav">
    <a class="active" href="#">ABOUT ME</a><a href="#">VIDEOS</a><a href="#">SOCIAL MEDIA</a><a href="#">BLOG</a><a href="#">GALLERY</a><a href="#">CONTACT ME</a>
  </nav>
</header>

<div class="abs hero" role="img" aria-label="Traveller sitting on a hilltop overlooking misty mountains at sunset"></div>

<section class="destinations">
  <div class="abs tile t-santorini" style="left:187px;top:269px" role="img" aria-label="Santorini white houses above the sea"><span>SANTORINI</span></div>
  <div class="abs tile t-paris" style="left:362px;top:269px" role="img" aria-label="Eiffel Tower under blue sky"><span>PARIS</span></div>
  <div class="abs tile t-india" style="left:537px;top:269px" role="img" aria-label="Taj Mahal in morning haze"><span>INDIA</span></div>
  <div class="abs tile t-turkey" style="left:187px;top:386px" role="img" aria-label="White mosque arcade"><span>TURKEY</span></div>
  <div class="abs tile t-england" style="left:362px;top:386px" role="img" aria-label="Westminster bridge at dusk"><span>ENGLAND</span></div>
  <div class="abs tile t-germany" style="left:537px;top:386px" role="img" aria-label="Castle on a forested hill"><span>GERMANY</span></div>
  <div class="abs tile t-santorini" style="left:187px;top:504px" role="img" aria-label="Santorini white houses above the sea"><span>SANTORINI</span></div>
  <div class="abs tile t-paris" style="left:362px;top:504px" role="img" aria-label="Eiffel Tower under blue sky"><span>PARIS</span></div>
  <div class="abs tile t-india" style="left:537px;top:504px" role="img" aria-label="Taj Mahal in morning haze"><span>INDIA</span></div>
  <div class="abs tile t-turkey" style="left:187px;top:621px" role="img" aria-label="White mosque arcade"><span>TURKEY</span></div>
  <div class="abs tile t-england" style="left:362px;top:621px" role="img" aria-label="Westminster bridge at dusk"><span>ENGLAND</span></div>
  <div class="abs tile t-germany" style="left:537px;top:621px" role="img" aria-label="Castle on a forested hill"><span>GERMANY</span></div>
</section>

<section class="recent-videos">
  <h2 class="abs section-title">RECENT VIDEOS</h2>
  <div class="abs video v-main" role="img" aria-label="Tall ship sailing on calm sea">
    <svg width="24" height="28" viewBox="0 0 24 28"><path d="M2 2 L22 14 L2 26 Z" fill="#fff"/></svg></div>
  <div class="abs video v-dusk" role="img" aria-label="Sailboats anchored at dusk">
    <svg width="16" height="18" viewBox="0 0 16 18"><path d="M1 1 L15 9 L1 17 Z" fill="#fff"/></svg></div>
  <div class="abs video v-lake" role="img" aria-label="Hiker's boots above a turquoise lake">
    <svg width="16" height="18" viewBox="0 0 16 18"><path d="M1 1 L15 9 L1 17 Z" fill="#fff"/></svg></div>
  <div class="abs video v-town" role="img" aria-label="Coastal village lit at night">
    <svg width="16" height="18" viewBox="0 0 16 18"><path d="M1 1 L15 9 L1 17 Z" fill="#fff"/></svg></div>
  <div class="abs video v-all" role="img" aria-label="Hiker on a forest path"><span>ALL VIDEOS</span><b></b></div>
</section>

<footer>
  <div class="abs footer-rule"></div>
  <div class="abs brand footer-brand"><span class="brand-dot"></span><span class="brand-name">ROAMINGSPARROW</span></div>
  <nav class="abs footer-nav">
    <a href="#">ABOUT ME</a><a href="#">VIDEOS</a><a href="#">SOCIAL MEDIA</a><a href="#">BLOG</a><a href="#">GALLERY</a><a href="#">CONTACT ME</a>
  </nav>
  <div class="abs socials footer-socials">
    <a class="social" href="#"><i></i>Snapwell</a>
    <a class="social" href="#"><i></i>Palnook</a>
    <a class="social" href="#"><i></i>vidtrekhub</a>
  </div>
  <p class="abs copyright">COPYRIGHT © 2018 ROAMINGSPARROW</p>
</footer>
</body>
</html>
```